TRENDY & MODERN BUSINESS CARD DESIGN for Media Company *

I need a minimalistic - clean - modern and professional business card layout and design for MEDIA & PHOTOGRAPHY STUDIO.

We do NOT have a logo, and not really looking for one - but rather excellent typography and design. We would consider the 3 as a focal point.

We do personal and commercial photography.

Target Market(s)

Personal and commercial photography clientele

Contact Information for Business Card

KYT size - from kyt.com / size guidelines are enclosed in the brief

Font styles to use
Sans Serif

Colors
f78f20
eda3c7
cee9f5
0555a3
e667a6
fbf289

Requirements
Must have
• Clean lines - Modern layout
Nice to have
• All blue background as an option - use color palette in brief please.
Should not have
• Old fashion fonts and regular fonts.

```html
<!DOCTYPE html>
<html lang="en">
<head>
<meta charset="utf-8">
<title>Lumen &amp; Lane – Business Card</title>
<link rel="stylesheet" href="https://fonts.googleapis.com/css2?family=Open+Sans:wght@400;600&family=Roboto:wght@500;700&display=swap">
<style>
  :root {
    --brand-blue: #0555a3;
    --brand-blue-soft: #1a63ad;
    --brand-orange: #f78f20;
    --ink: #2b2b2b;
    --muted: #7a7a7a;
    --rule: #b5b5b5;
    --paper: #ffffff;
    --backdrop: #e9ebee;
  }
  * { box-sizing: border-box; margin: 0; padding: 0; }
  html, body { width: 1200px; height: 782px; overflow: hidden; }
  body {
    background: var(--backdrop);
    font-family: "Open Sans", Arial, sans-serif;
    display: flex;
    align-items: center;
    justify-content: center;
    gap: 40px;
  }
  .card {
    width: 540px;
    height: 309px;
    position: relative;
    overflow: hidden;
    box-shadow: 0 6px 18px rgba(0,0,0,.18);
  }

  /* Front */
  .card-front { background: var(--paper); }
  .brand {
    position: absolute;
    left: 30px; top: 44px;
    width: 220px;
    display: flex;
    flex-direction: column;
    align-items: center;
  }
  .brand-dot {
    width: 74px; height: 74px;
    border-radius: 50%;
    background: var(--brand-blue);
    margin-bottom: 14px;
  }
  .brand-name {
    font-family: "Roboto", Arial, sans-serif;
    font-weight: 500;
    font-size: 24px;
    color: var(--brand-blue);
    white-space: nowrap;
  }
  .brand-tagline {
    margin-top: 4px;
    font-size: 9.5px;
    letter-spacing: 1.6px;
    color: var(--muted);
  }
  .divider {
    position: absolute;
    left: 268px; top: 46px;
    width: 1px; height: 172px;
    background: var(--rule);
  }
  .contact {
    position: absolute;
    left: 288px; top: 60px;
    right: 16px;
  }
  .contact-name {
    font-family: "Roboto", Arial, sans-serif;
    font-weight: 700;
    font-size: 19px;
    color: var(--brand-blue);
    text-transform: uppercase;
    letter-spacing: .4px;
  }
  .contact-role {
    font-size: 14px;
    color: var(--brand-orange);
    margin-bottom: 10px;
  }
  .contact-line {
    display: flex;
    align-items: center;
    gap: 6px;
    font-size: 13.5px;
    color: var(--ink);
    line-height: 1.35;
  }
  .contact-line svg { width: 13px; height: 13px; flex: none; fill: var(--brand-blue); }
  .contact-address {
    margin-top: 4px;
    font-size: 13.5px;
    color: var(--ink);
    line-height: 1.35;
    font-style: normal;
  }
  .city-band {
    position: absolute;
    left: 0; right: 0; bottom: 0;
    height: 58px;
    background: var(--brand-blue);
    display: flex;
    align-items: center;
    justify-content: center;
    gap: 10px;
    color: var(--paper);
    font-size: 14.5px;
    list-style: none;
  }
  .city-band li + li::before {
    content: "";
    display: inline-block;
    width: 6px; height: 6px;
    border-radius: 50%;
    background: var(--brand-orange);
    margin-right: 10px;
    vertical-align: middle;
  }

  /* Back */
  .card-back { background: var(--brand-blue); }
  .back-pattern {
    position: absolute; inset: 0;
    background: linear-gradient(135deg, var(--brand-blue-soft), var(--brand-blue));
  }
  .back-mark {
    position: absolute;
    right: 28px; bottom: 30px;
    display: flex;
    align-items: center;
    gap: 10px;
  }
  .back-mark-dot {
    width: 44px; height: 44px;
    border-radius: 50%;
    background: var(--paper);
  }
  .back-mark-name {
    font-family: "Roboto", Arial, sans-serif;
    font-weight: 500;
    font-size: 18px;
    color: var(--paper);
  }
</style>
</head>
<body>
  <section class="card card-front">
    <div class="brand">
      <div class="brand-dot"></div>
      <div class="brand-name">Lumen &amp; Lane</div>
      <div class="brand-tagline">Stories Told in Light.</div>
    </div>
    <div class="divider"></div>
    <div class="contact">
      <div class="contact-name">Marisol Vega</div>
      <div class="contact-role">Founder &amp; Media Director</div>
      <div class="contact-line">
        <svg viewBox="0 0 24 24" aria-hidden="true"><path d="M6.6 10.8a15.1 15.1 0 0 0 6.6 6.6l2.2-2.2a1 1 0 0 1 1-.25 11.4 11.4 0 0 0 3.6.57 1 1 0 0 1 1 1V20a1 1 0 0 1-1 1A17 17 0 0 1 3 4a1 1 0 0 1 1-1h3.5a1 1 0 0 1 1 1c0 1.25.2 2.45.57 3.57a1 1 0 0 1-.25 1z"/></svg>
        <span>(305) 555-0148</span>
      </div>
      <div class="contact-line">
        <svg viewBox="0 0 24 24" aria-hidden="true"><path d="M2 5h20v14H2z M3.5 6.5 12 13l8.5-6.5" fill="none" stroke="#0555a3" stroke-width="2"/><path d="M2 5h20v2l-10 7L2 7z"/></svg>
        <span>mari@lumenlane.com</span>
      </div>
      <address class="contact-address">2400 Coral Way<br>9th Floor, Miami, FL 33145</address>
    </div>
    <ul class="city-band">
      <li>Miami</li>
      <li>New York</li>
      <li>Las Vegas</li>
      <li>Cancun</li>
      <li>Roma</li>
    </ul>
  </section>

  <section class="card card-back">
    <div class="back-pattern" role="img" aria-label="Faint tone-on-blue repeating brand pattern"></div>
    <div class="back-mark">
      <div class="back-mark-dot"></div>
      <div class="back-mark-name">Lumen &amp; Lane</div>
    </div>
  </section>
</body>
</html>
```